Harlow Ironworks Business Card

We need a business card design for a new small metal fabrication business in rural NSW, Australia.

The business (Harlow Ironworks) is owner operated by a man with the initials KB - much of the branding comes from this name.

Harlow Ironworks designs, engineers, repairs and manufactures a range of custom, quality metal works including vehicle trays, agricultural machinery impliments, trailers, wood splitters, fire pits, furniture etc.

The brand position focuses on custom work of the highest quality.

Business card design should show quality, attention to detail and stand out among a mass of business cards.

Logos are in the files

The grey color may be changed on the logo if required to stand out more.

There is an image attached of a simple card that is liked because it is clean, clear, simple, masculine and effective. It says 'quality'. As most of the work we do is custom it would be good to have the business card speak to this.

Target Market(s)

Rural and regional based Australians. Primarily adult male 25-60 yrs. Primary production / rural / travelling lifestyle.

Industry/Entity Type

Metal Fabrication

Contact Information for Business Card

The words 'custom quality fabrications' would be great somewhere perhaps on the backside (not on the information side)
Name
title
Phone: 0418 539 746 and (02) 6193 4827
email: info@harlowiw.com.au
www.harlowiw.com.au

address (2 lines)

Requirements
Nice to have
• Background colour should be very navy blue or black.
Should not have
• NO orange and blue combinations.
• Navy is OK

```html
<!DOCTYPE html>
<html lang="en">
<head>
<meta charset="utf-8">
<title>Harlow Ironworks Business Card</title>
<link href="https://fonts.googleapis.com/css2?family=Michroma&family=Open+Sans:wght@400;600;700&display=swap" rel="stylesheet">
<style>
  :root {
    --backdrop: #2a2422;
    --card-white: #ffffff;
    --card-grey: #a6a6a6;
    --brand-grey: #9b9b9b;
    --brand-green: #5cc23a;
    --text-white: #ffffff;
  }
  * { margin: 0; padding: 0; box-sizing: border-box; }
  html, body {
    width: 1200px; height: 900px; overflow: hidden;
    background: var(--backdrop);
  }
  .stage {
    position: relative; width: 1200px; height: 900px;
    display: flex; align-items: center; justify-content: center; gap: 40px;
  }
  .card {
    position: relative; width: 540px; height: 310px; overflow: hidden;
    box-shadow: 0 12px 30px rgba(0,0,0,.45);
  }
  /* Front side */
  .card-front { background: var(--card-white); }
  .front-brand {
    position: absolute; left: 0; right: 0; top: 70px;
    display: flex; align-items: center; justify-content: center; gap: 14px;
  }
  .brand-square {
    width: 34px; height: 34px; background: var(--brand-green);
  }
  .brand-name {
    font-family: "Michroma", sans-serif; font-size: 27px; letter-spacing: 1px;
    color: var(--brand-grey); text-transform: uppercase; line-height: 1;
  }
  .front-info {
    position: absolute; left: 0; right: 0; bottom: 0; height: 118px;
    background: var(--card-grey);
    border-top: 3px solid var(--brand-green);
    display: flex; align-items: center; padding: 0 34px; color: var(--text-white);
    font-family: "Open Sans", sans-serif;
  }
  .person { width: 170px; text-align: right; padding-right: 18px; }
  .person-name { font-size: 21px; font-weight: 700; line-height: 1.15; }
  .person-title { font-size: 13px; }
  .divider { width: 1px; height: 62px; background: var(--text-white); opacity: .8; }
  .contact-list { list-style: none; padding-left: 18px; font-size: 13px; }
  .contact-list li { display: flex; align-items: center; gap: 8px; line-height: 20px; }
  .contact-icon { width: 13px; height: 13px; flex: none; }
  /* Back side */
  .card-back { background: var(--card-grey); }
  .back-brand {
    position: absolute; left: 0; right: 0; top: 104px;
    display: flex; align-items: center; justify-content: center;
  }
  .back-brand .brand-name { color: var(--text-white); font-size: 28px; }
  .tagline {
    position: absolute; left: 0; right: 0; bottom: 46px; text-align: center;
    font-family: "Michroma", sans-serif; font-size: 10.5px; letter-spacing: 2px;
    color: var(--text-white); text-transform: uppercase;
  }
</style>
</head>
<body>
<main class="stage">
  <section class="card card-front" aria-label="Business card, front">
    <div class="front-brand">
      <span class="brand-square"></span>
      <span class="brand-name">Harlow Ironworks</span>
    </div>
    <div class="front-info">
      <div class="person">
        <p class="person-name">Kieran Bell</p>
        <p class="person-title">Managing Director</p>
      </div>
      <span class="divider"></span>
      <ul class="contact-list">
        <li>
          <svg class="contact-icon" viewBox="0 0 16 16"><rect width="16" height="16" rx="3" fill="#fff"/><path d="M5 3.5l2 2-1.2 1.3a6 6 0 0 0 3.4 3.4L10.5 9l2 2-1.5 1.5C7.5 12.5 3.5 8.5 3.5 5z" fill="#a6a6a6"/></svg>
          0418 539 746 | (02) 6193 4827
        </li>
        <li>
          <svg class="contact-icon" viewBox="0 0 16 16"><rect width="16" height="16" rx="3" fill="#fff"/><rect x="3" y="4.5" width="10" height="7" fill="none" stroke="#a6a6a6" stroke-width="1.2"/><path d="M3 4.5l5 4 5-4" fill="none" stroke="#a6a6a6" stroke-width="1.2"/></svg>
          info@harlowiw.com.au
        </li>
        <li>
          <svg class="contact-icon" viewBox="0 0 16 16"><rect width="16" height="16" rx="3" fill="#fff"/><circle cx="8" cy="8" r="4.8" fill="none" stroke="#a6a6a6" stroke-width="1.1"/><ellipse cx="8" cy="8" rx="2" ry="4.8" fill="none" stroke="#a6a6a6" stroke-width="1"/><path d="M3.2 8h9.6" stroke="#a6a6a6" stroke-width="1"/></svg>
          www.harlowiw.com.au
        </li>
      </ul>
    </div>
  </section>

  <section class="card card-back" aria-label="Business card, back">
    <div class="back-brand">
      <span class="brand-name">Harlow Ironworks</span>
    </div>
    <p class="tagline">The words 'Custom Quality Fabrications</p>
  </section>
</main>
</body>
</html>
```